Package design for small honey and vegetable farm

I would like to have a unique design for the packaging of our honey and vegetables. I have attached the logo from our farm "Willow Creek Acres" that should be on the packaging for both the honey and the vegetables

For the honey the writing, "100% pure organic honey" must be on the packaging in some place. As well as "from the busy bees at Willow Creek Acres". I have attached some designs that I like.

For the vegetables. The design will need to go on a box like the one in the attached image. The phrase "Organically Grown" should be on the package. I would like the background color of the package to be black. I think I would also like to see some stylized vegetables (tomatoes in particular) on the package.

I would like to be able to get all the colors (RGB) used in the designs so I can pass them on to printers.

Industry/Entity Type

Farm

Colors
fbee3e

Requirements
Must have
• For the honey, the package it must say "100% pure organic honey".
• For the vegetables I would like the background color to be black. I would also like some stylized vegetables (tomatoes in particular) added to the package.

```html
<!DOCTYPE html>
<html lang="en">
<head>
<meta charset="utf-8">
<title>Willow Creek Acres – Honey Label and Vegetable Box</title>
<link rel="stylesheet" href="https://fonts.googleapis.com/css2?family=Montserrat:wght@500;600;700&family=Lora:ital@1&display=swap">
<style>
  :root {
    --honey-yellow: #fbee3e;
    --label-gold: #f2d63a;
    --panel-black: #1c1712;
    --kraft-cream: #e6dccb;
    --page-bg: #f3f1ec;
    --veg-red: #c8321f;
    --veg-orange: #e0802a;
    --veg-green: #5f8f2e;
  }
  * { margin: 0; padding: 0; box-sizing: border-box; }
  html, body { width: 801px; height: 1200px; overflow: hidden; }
  body {
    background: var(--page-bg);
    font-family: "Montserrat", sans-serif;
    position: relative;
  }

  /* Honey jar label */
  .honey-label {
    position: absolute;
    left: 160px; top: 150px;
    width: 481px; height: 300px;
    background: var(--panel-black);
    color: var(--label-gold);
    text-align: center;
    padding-top: 36px;
  }
  .purity-mark {
    display: flex; align-items: center; justify-content: center; gap: 14px;
  }
  .purity-mark .rules { display: flex; flex-direction: column; gap: 4px; }
  .purity-mark .rules span { display: block; height: 2px; background: var(--label-gold); }
  .purity-mark .rules.left span:nth-child(1) { width: 38px; }
  .purity-mark .rules.left span:nth-child(2) { width: 46px; }
  .purity-mark .rules.left span:nth-child(3) { width: 54px; }
  .purity-mark .rules.right span:nth-child(1) { width: 38px; margin-left: auto; }
  .purity-mark .rules.right span:nth-child(2) { width: 46px; }
  .purity-mark .rules.right span:nth-child(3) { width: 54px; }
  .purity-title { font-weight: 700; font-size: 24px; letter-spacing: 1px; line-height: 1; }
  .purity-sub { font-weight: 600; font-size: 11px; letter-spacing: 1.5px; margin-top: 4px; }

  .farm-name {
    margin-top: 52px;
    display: flex; align-items: center; justify-content: center; gap: 12px;
    font-weight: 600; font-size: 30px; letter-spacing: 1px;
  }
  .farm-name .dot {
    width: 14px; height: 14px; border-radius: 50%;
    background: var(--label-gold);
  }
  .tagline {
    margin-top: 56px;
    font-family: "Lora", serif; font-style: italic;
    font-size: 14px; line-height: 1.35;
  }

  /* Vegetable box front panel */
  .veg-box-panel {
    position: absolute;
    left: 60px; top: 660px;
    width: 681px; height: 380px;
  }
  .veg-box-panel svg { display: block; }
  .box-slogan {
    position: absolute;
    left: 150px; top: 44px;
    color: var(--honey-yellow);
    font-weight: 700; font-size: 30px; line-height: 1.05;
    letter-spacing: 1px; text-align: center;
  }
</style>
</head>
<body>

  <section class="honey-label">
    <div class="purity-mark">
      <div class="rules left"><span></span><span></span><span></span></div>
      <div>
        <div class="purity-title">100% PURE</div>
        <div class="purity-sub">ORGANIC HONEY</div>
      </div>
      <div class="rules right"><span></span><span></span><span></span></div>
    </div>
    <div class="farm-name"><span class="dot"></span>Willow Creek Acres</div>
    <p class="tagline">from the busy bees at<br>Willow Creek Acres</p>
  </section>

  <section class="veg-box-panel">
    <svg width="681" height="380" viewBox="0 0 681 380">
      <defs>
        <linearGradient id="veg-tones" x1="0" y1="1" x2="1" y2="0">
          <stop offset="0" stop-color="var(--veg-red)"/>
          <stop offset="0.35" stop-color="var(--veg-orange)"/>
          <stop offset="0.65" stop-color="var(--veg-green)"/>
          <stop offset="1" stop-color="var(--veg-red)"/>
        </linearGradient>
      </defs>
      <rect class="panel-ground" width="681" height="380" fill="var(--panel-black)"/>
      <path class="kraft-area" d="M150,380 C230,210 430,120 681,95 L681,380 Z" fill="var(--kraft-cream)"/>
      <g role="img" aria-label="Fresh vegetables: tomatoes, peppers, onions, courgettes and herbs">
        <path class="veg-artwork" d="M210,380 C290,240 450,170 681,150 L681,380 Z" fill="url(#veg-tones)" opacity="0.9"/>
      </g>
      <path class="gold-curve" d="M132,380 C212,200 420,105 681,80" fill="none" stroke="var(--honey-yellow)" stroke-width="4"/>
    </svg>
    <div class="box-slogan">ORGANICALLY<br>GROWN</div>
  </section>

</body>
</html>
```